The Lumo-Hub for Rescue Instruction + Venue Readiness Post Card

Hi! I am a new business that is Licensed Training Provider to the National Bluefield Aid. We teach private CPR/AED, First Aid and a variety of other emergency training courses to the general public! Our goal is to get into businesses of all sizes from the mom and pops store to corporate offices of Manhattan. We can do private classes in your home and no office space is to small! We even have a school assembly program that teaches "Hands Only CPR" for children. I'm looking to make a post card to hand out that can easily explain what we are doing…that might have some good visuals that catch your eye as well. I def want to use The Lumo Hub logo in it that I have attached. Im not necessarily married to any of the other images. You can check out our website www.lumohubinstruct.example for more information and you can use any of the images on there as well if you would like. I will give you free reign to find any cool photo stock image that you might think fits with what I'm trying to do. Hopefully you can help!
Updates

Also feel free to use any other photos that you might find that you think fit our cause for teaching CPR/First aid etc!! Thanks!

Thank you all for your hard work. I actually like many of these designs and really torn! I will be making some decisions in the next day or so. Thank you! Dale

Industry/Entity Type

Training

```html
<!DOCTYPE html>
<html lang="en">
<head>
<meta charset="utf-8">
<title>The Lumo Hub – Rescue Instruction Post Card</title>
<link rel="stylesheet" href="https://fonts.googleapis.com/css2?family=Roboto+Condensed:ital,wght@0,400;0,700;1,400;1,700&family=Quicksand:wght@400&display=swap">
<style>
  :root {
    --ink: #231f20;
    --band: #262223;
    --red: #d71f26;
    --red-deep: #a8141b;
    --yellow: #f7c418;
    --white: #ffffff;
    --pulse: #8fd3e0;
    --board: #1e1e1e;
    --frame: #d98b1e;
  }
  * { margin: 0; padding: 0; box-sizing: border-box; }
  html, body { width: 1200px; height: 930px; overflow: hidden; background: var(--white); }
  body { font-family: "Roboto Condensed", "Arial Narrow", sans-serif; color: var(--ink); }

  .postcard { position: relative; width: 1200px; height: 930px; background: var(--white); }

  .masthead {
    position: absolute; left: 30px; top: 30px; width: 1140px; height: 142px;
    background: var(--band); text-align: center;
  }
  .brand-name {
    font-family: "Quicksand", sans-serif; font-weight: 400;
    color: var(--white); font-size: 76px; letter-spacing: 2px;
    line-height: 1; padding-top: 22px;
  }
  .brand-tagline {
    color: var(--red); font-weight: 700; font-size: 18px; letter-spacing: 0.5px;
    margin-top: 6px; padding-left: 260px;
  }

  .hero {
    position: absolute; left: 30px; top: 172px; width: 1140px; height: 588px;
    background: linear-gradient(90deg, var(--red) 0%, var(--red) 55%, var(--red-deep) 100%);
    overflow: hidden;
  }
  .headline { position: absolute; left: 42px; top: 20px; line-height: 1.05; }
  .headline-main { font-size: 47px; font-weight: 400; color: var(--ink); }
  .headline-main strong { color: var(--white); font-weight: 700; }
  .headline-sub { font-size: 37px; margin-top: 8px; color: var(--ink); }
  .headline-sub strong { color: var(--white); font-weight: 700; }

  .course-panel {
    position: absolute; left: 40px; top: 178px; width: 428px; height: 386px;
    background: #111; padding: 14px 12px;
  }
  .course-heading { color: var(--red); font-weight: 700; font-size: 18px; margin-bottom: 2px; }
  .course-list { list-style: none; margin-bottom: 4px; }
  .course-list li {
    color: var(--white); font-style: italic; font-size: 16px; line-height: 24px;
    display: flex; align-items: center; gap: 6px;
  }
  .course-list svg { flex: none; }

  .slogan-board {
    position: absolute; left: 356px; top: 408px; width: 212px; height: 144px;
    background: var(--board); border: 7px solid var(--frame);
    transform: rotate(-4deg);
  }

  .team-photo {
    position: absolute; left: 540px; top: 8px; width: 600px; height: 548px;
    background: linear-gradient(180deg, rgba(230,215,200,0.35) 0%, rgba(120,120,125,0.55) 60%, rgba(40,40,40,0.7) 100%);
  }

  .reach-band { position: absolute; left: 0; top: 548px; width: 1140px; height: 40px; }
  .reach-text {
    position: absolute; right: 26px; top: 558px;
    color: var(--red); font-weight: 700; font-style: italic; font-size: 21px;
  }

  .footer {
    position: absolute; left: 30px; top: 760px; width: 1140px; height: 140px;
    background: var(--band);
  }
  .contact { position: absolute; left: 40px; top: 12px; color: var(--white); font-weight: 700; font-size: 18px; line-height: 24px; }
  .contact-name { font-style: italic; font-size: 22px; }
  .contact-web { display: flex; align-items: center; gap: 38px; font-style: italic; }
  .web-square { width: 20px; height: 20px; background: #3b5a98; }

  .partner-badge {
    position: absolute; top: 22px; height: 96px; background: var(--white); border-radius: 6px;
  }
  .partner-one { left: 632px; width: 206px; }
  .partner-two { left: 867px; width: 248px; }
</style>
</head>
<body>
<main class="postcard">
  <header class="masthead">
    <div class="brand-name">THE LUMO HUB</div>
    <div class="brand-tagline">RESCUE INSTRUCTION + VENUE READINESS</div>
  </header>

  <section class="hero">
    <div class="headline">
      <div class="headline-main">Learn to <strong>SAVE LIFE</strong> today!</div>
      <div class="headline-sub">Advanced First Aid,</div>
      <div class="headline-sub"><strong>CPR &amp; AED</strong> Training Courses</div>
    </div>

    <div class="course-panel">
      <div class="course-heading">Classes Offered:</div>
      <ul class="course-list">
        <li><svg width="22" height="14" viewBox="0 0 22 14"><polyline points="0,7 6,7 8,2 11,12 13,4 15,7 22,7" fill="none" stroke="var(--pulse)" stroke-width="1.6"/></svg>CPR for the Professional Rescuer &amp; Health Care Provider</li>
        <li><svg width="22" height="14" viewBox="0 0 22 14"><polyline points="0,7 6,7 8,2 11,12 13,4 15,7 22,7" fill="none" stroke="var(--pulse)" stroke-width="1.6"/></svg>Automatic External Defibrillator (AED)</li>
        <li><svg width="22" height="14" viewBox="0 0 22 14"><polyline points="0,7 6,7 8,2 11,12 13,4 15,7 22,7" fill="none" stroke="var(--pulse)" stroke-width="1.6"/></svg>Lay Responder CPR</li>
        <li><svg width="22" height="14" viewBox="0 0 22 14"><polyline points="0,7 6,7 8,2 11,12 13,4 15,7 22,7" fill="none" stroke="var(--pulse)" stroke-width="1.6"/></svg>Infant CPR/ Choking for new parents</li>
        <li><svg width="22" height="14" viewBox="0 0 22 14"><polyline points="0,7 6,7 8,2 11,12 13,4 15,7 22,7" fill="none" stroke="var(--pulse)" stroke-width="1.6"/></svg>First Aid</li>
        <li><svg width="22" height="14" viewBox="0 0 22 14"><polyline points="0,7 6,7 8,2 11,12 13,4 15,7 22,7" fill="none" stroke="var(--pulse)" stroke-width="1.6"/></svg>Emergency Response</li>
        <li><svg width="22" height="14" viewBox="0 0 22 14"><polyline points="0,7 6,7 8,2 11,12 13,4 15,7 22,7" fill="none" stroke="var(--pulse)" stroke-width="1.6"/></svg>Lifeguard Training</li>
        <li><svg width="22" height="14" viewBox="0 0 22 14"><polyline points="0,7 6,7 8,2 11,12 13,4 15,7 22,7" fill="none" stroke="var(--pulse)" stroke-width="1.6"/></svg>Oxygen Administration</li>
        <li><svg width="22" height="14" viewBox="0 0 22 14"><polyline points="0,7 6,7 8,2 11,12 13,4 15,7 22,7" fill="none" stroke="var(--pulse)" stroke-width="1.6"/></svg>Disaster Preparedness</li>
        <li><svg width="22" height="14" viewBox="0 0 22 14"><polyline points="0,7 6,7 8,2 11,12 13,4 15,7 22,7" fill="none" stroke="var(--pulse)" stroke-width="1.6"/></svg>Bloodborne Pathogens</li>
      </ul>
      <div class="course-heading">Specialized Programs for Chools:</div>
      <ul class="course-list">
        <li><svg width="22" height="14" viewBox="0 0 22 14"><polyline points="0,7 6,7 8,2 11,12 13,4 15,7 22,7" fill="none" stroke="var(--pulse)" stroke-width="1.6"/></svg>First Aid for students</li>
        <li><svg width="22" height="14" viewBox="0 0 22 14"><polyline points="0,7 6,7 8,2 11,12 13,4 15,7 22,7" fill="none" stroke="var(--pulse)" stroke-width="1.6"/></svg>CPR for students</li>
        <li><svg width="22" height="14" viewBox="0 0 22 14"><polyline points="0,7 6,7 8,2 11,12 13,4 15,7 22,7" fill="none" stroke="var(--pulse)" stroke-width="1.6"/></svg>First Aid and CPR for students</li>
      </ul>
    </div>

    <div class="team-photo" role="img" aria-label="Photo of a smiling businesswoman, a construction worker in a hard hat and a young man in a grey t-shirt"></div>

    <div class="slogan-board" role="img" aria-label="Chalkboard with hand lettering reading: Are you prepared?"></div>

    <svg class="reach-band" viewBox="0 0 1140 40" preserveAspectRatio="none" aria-hidden="true">
      <path d="M40,40 C60,12 80,10 120,10 L1140,10 L1140,40 Z" fill="var(--yellow)"/>
    </svg>
    <div class="reach-text">You don’t have to come to us...We will come to you!</div>
  </section>

  <footer class="footer">
    <div class="contact">
      <div>For more information on booking the Lumo-Hub for your event:</div>
      <div class="contact-name">Dale Marsh</div>
      <div>Email:&nbsp; lumohub911@mailbox.example</div>
      <div>Phone: 555.014.2290</div>
      <div class="contact-web"><span class="web-square"></span>www.social.example/TheLumoHub4EmergencyPrepardness</div>
    </div>
    <div class="partner-badge partner-one" role="img" aria-label="Partner badge: Northfield Cardiac Guild"></div>
    <div class="partner-badge partner-two" role="img" aria-label="Partner badge: National Bluefield Aid"></div>
  </footer>
</main>
</body>
</html>
```